Tamber Pursuit Circuit 2017 schedule poster

A poster for the schedule of our events for the year, letting people know that they can bring their car and drive it on a track. instructors are available. included different car shots from the track. these can be included or not up to the artist's discretion. celebrating over 50 years as a club.
Updates

Project Deadline Extended
Reason: Just received dates, my apologies

Target Market(s)

young adult- retiree's

Industry/Entity Type

Car Racing

Contact Information for Business Card

A small card with the dates and Marlowe Sports Car Club logo the website MSCCVELDANE.ORG is a must, if possible any of the other information that is in the must-haves.

Font styles to use
Serif

Colors
33a6d7
85cae6
3176b5
85acd3
ffffff

Requirements
Must have
• 2017 dates, Sponsors, the website "MSCCVELDANE.ORG" , it say "2017 Tamber Pursuit Circuit", and "drive your car on a track". and say where, "Pellway Basin Sports Park". Vernal Trekday March 24-26, Event #2 April 22-23, Event #3 May 20-21, Event #4 June 24-25, Brindle Ponds Ridgerun June 11-12, Event #5 July 29-30, Event #6 August 19-20, Event #7 September 9-10, Autumn Trekday October 6-8
Nice to have
• easy to read and contrast

```html
<!DOCTYPE html>
<html lang="en">
<head>
<meta charset="utf-8">
<title>2017 Tamber Pursuit Circuit – Schedule Poster</title>
<link href="https://fonts.googleapis.com/css2?family=Oswald:wght@400;500;600;700&family=Montserrat:wght@500&display=swap" rel="stylesheet">
<style>
  :root {
    --page-bg: #e8e8e8;
    --navy: #1e4c86;
    --blue: #3176b5;
    --blue-mid: #4a86c2;
    --sky: #85acd3;
    --white: #ffffff;
    --ink: #2d2d2d;
    --grey: #6e6e6e;
    --rule: rgba(255,255,255,0.45);
  }
  * { box-sizing: border-box; margin: 0; padding: 0; }
  html, body { width: 1200px; height: 1200px; overflow: hidden; background: var(--page-bg); }
  .poster {
    position: absolute; left: 208px; top: 30px; width: 784px; height: 1140px;
    background: linear-gradient(180deg, var(--navy) 0%, var(--blue) 22%, var(--sky) 38%, #e6eef6 52%, var(--white) 62%);
    overflow: hidden; font-family: 'Oswald', sans-serif;
    box-shadow: 0 4px 14px rgba(0,0,0,0.25);
  }
  .title {
    position: absolute; top: 52px; left: 0; width: 100%; text-align: center;
    color: var(--white); font-weight: 700; text-transform: uppercase;
    font-size: 88px; line-height: 92px; letter-spacing: -1px;
    text-shadow: 0 3px 6px rgba(0,0,0,0.35);
  }
  .car-photo {
    position: absolute; left: 94px; top: 280px; width: 616px; height: 330px;
    border-radius: 46% 46% 30% 30% / 40% 40% 22% 22%;
    background: radial-gradient(ellipse at 50% 45%, #2c3f8e 0%, #1d2a66 55%, rgba(29,42,102,0.2) 100%);
  }
  .tagline {
    position: absolute; top: 640px; width: 100%; text-align: center;
    color: var(--ink); font-weight: 500; font-size: 66px; line-height: 76px;
    text-transform: uppercase; letter-spacing: -0.5px;
  }
  .meta { position: absolute; width: 100%; text-align: center; font-size: 27px; line-height: 34px; text-transform: uppercase; }
  .meta .label { color: var(--ink); font-weight: 500; }
  .meta .value { color: var(--blue); font-weight: 400; }
  .meta.date { top: 726px; left: -20px; }
  .meta.place { top: 772px; left: 20px; }
  .schedule {
    position: absolute; top: 825px; height: 182px; border-radius: 6px; overflow: hidden;
    display: grid; background: var(--grey);
  }
  .schedule.first { left: 21px; width: 381px; grid-template-columns: 246px 1fr; grid-template-rows: repeat(5, 1fr); }
  .schedule.second { left: 423px; width: 338px; grid-template-columns: 155px 1fr; grid-template-rows: repeat(4, 1fr); }
  .schedule .event, .schedule .when {
    display: flex; align-items: center; color: var(--white); font-weight: 600; font-size: 23px;
    border-bottom: 1px solid var(--rule); padding-left: 14px; white-space: nowrap;
  }
  .schedule .event { background: var(--blue); }
  .schedule .when { padding-left: 10px; }
  .schedule .last { border-bottom: none; }
  .sponsors {
    position: absolute; top: 1030px; left: 20px; right: 20px; height: 44px;
    display: flex; justify-content: space-between; align-items: center;
  }
  .sponsor { display: flex; align-items: center; gap: 5px; color: var(--navy); font-weight: 500; font-size: 15px; text-transform: uppercase; }
  .sponsor .dot { width: 12px; height: 12px; border-radius: 50%; background: var(--blue); }
  .footer-rule { position: absolute; top: 1082px; left: 0; width: 100%; height: 3px; background: var(--sky); }
  .footer {
    position: absolute; top: 1088px; left: 0; width: 100%; height: 52px; background: var(--blue);
    color: var(--white); font-family: 'Montserrat', sans-serif; font-weight: 500; font-size: 21px;
    letter-spacing: 3px; display: flex; align-items: center; justify-content: center;
  }
</style>
</head>
<body>
  <main class="poster">
    <h1 class="title">2017 Tamber<br>Pursuit Circuit</h1>
    <div class="car-photo" role="img" aria-label="Photo of a blue sports car driving on the track"></div>
    <h2 class="tagline">Drive your car on a track</h2>
    <p class="meta date"><span class="label">Date :</span> <span class="value">22 March – 8 October, 2017</span></p>
    <p class="meta place"><span class="label">Place :</span> <span class="value">Pellway Basin Sports Park</span></p>

    <section class="schedule first">
      <div class="event">Vernal Trekday</div><div class="when">24-26 March</div>
      <div class="event">Event - 2</div><div class="when">22-23 April</div>
      <div class="event">Event - 3</div><div class="when">20-21 May</div>
      <div class="event">Event - 4</div><div class="when">24-25 June</div>
      <div class="event last">Brindle Ponds Ridgerun</div><div class="when last">11-12 June</div>
    </section>
    <section class="schedule second">
      <div class="event">Event - 5</div><div class="when">29-30 July</div>
      <div class="event">Event - 6</div><div class="when">19-20 August</div>
      <div class="event">Event - 7</div><div class="when">9-10 September</div>
      <div class="event last">Autumn Trekday</div><div class="when last">06-08 October</div>
    </section>

    <div class="sponsors">
      <span class="sponsor">Tallyard Signs</span>
      <span class="sponsor"><span class="dot"></span>Ferncrest Motors</span>
      <span class="sponsor">Marlowe SCC</span>
      <span class="sponsor">Halvern Auto</span>
      <span class="sponsor">Quillbrook Cars</span>
      <span class="sponsor">Orrin Detailing</span>
    </div>

    <div class="footer-rule"></div>
    <footer class="footer">www.msccveldane.org</footer>
  </main>
</body>
</html>
```